Health Care Company with Logo Needs Business Cards designed

We are a luxury behavioral health company looking for business cards design we already have a logo and are looking for someone to design a sophisticated luxurious looking business card. Please note that Card design should be captivating just like the logo and also encompass the logo color

Industry/Entity Type

Healthcare

Contact Information for Business Card

Logo,company name, tagline, my name and title, contact details, and physical address

```html
<!DOCTYPE html>
<html lang="en">
<head>
<meta charset="utf-8">
<title>Marlow Behavioral Health – Business Card</title>
<link href="https://fonts.googleapis.com/css2?family=Arimo:wght@400;700&display=swap" rel="stylesheet">
<style>
  :root {
    --stage: #2b2b2d;
    --card: #1e1e20;
    --purple: #8a3fa6;
    --blue: #29a8e0;
    --green: #8cc63f;
    --ink: #f2f2f2;
    --muted: #bdbdc2;
  }
  * { margin: 0; padding: 0; box-sizing: border-box; }
  html, body { width: 1200px; height: 900px; overflow: hidden; }
  body {
    background: var(--stage);
    display: flex;
    flex-direction: column;
    align-items: center;
    justify-content: center;
    gap: 56px;
    font-family: "Arimo", Arial, sans-serif;
  }
  .card {
    position: relative;
    width: 630px;
    height: 360px;
    background: var(--card);
    border-radius: 22px;
    overflow: hidden;
    box-shadow: 0 14px 30px rgba(0,0,0,.45);
  }
  .card::after {
    content: "";
    position: absolute;
    left: 0; right: 0; bottom: 0;
    height: 12px;
    background: var(--blue);
  }
  .lockup { display: flex; align-items: center; gap: 14px; white-space: nowrap; }
  .lockup__mark { background: var(--purple); flex: none; }
  .lockup__name { font-weight: 700; color: var(--purple); line-height: 1; }
  .tagline { font-weight: 400; color: var(--muted); }

  /* Logo side */
  .card--back { display: flex; flex-direction: column; align-items: center; justify-content: center; gap: 16px; padding-bottom: 12px; }
  .card--back .lockup__mark { width: 40px; height: 40px; }
  .card--back .lockup__name { font-size: 40px; }
  .card--back .tagline { font-size: 17px; }

  /* Details side */
  .card--front { display: flex; align-items: center; padding: 0 36px 12px 36px; }
  .card--front .brand { width: 250px; display: flex; flex-direction: column; gap: 8px; }
  .card--front .lockup { gap: 8px; }
  .card--front .lockup__mark { width: 16px; height: 16px; }
  .card--front .lockup__name { font-size: 18px; }
  .card--front .tagline { font-size: 11px; padding-left: 24px; }
  .divider { width: 1px; height: 210px; background: var(--green); margin: 0 28px 0 14px; flex: none; }
  .details { color: var(--ink); font-size: 14px; line-height: 1.45; }
  .details__name { font-weight: 700; font-size: 26px; color: var(--purple); text-transform: uppercase; letter-spacing: .02em; line-height: 1.1; }
  .details__title { margin-bottom: 10px; font-size: 15px; }
  .details__address { margin-bottom: 10px; }
  .contact { list-style: none; }
  .contact li { display: flex; align-items: center; gap: 9px; }
  .contact svg { width: 14px; height: 14px; fill: var(--blue); flex: none; }
</style>
</head>
<body>

  <section class="card card--back" aria-label="Business card, logo side">
    <div class="lockup">
      <span class="lockup__mark" aria-hidden="true"></span>
      <span class="lockup__name">Marlow Behavioral Health</span>
    </div>
    <p class="tagline">Caring for mind, body and renewal</p>
  </section>

  <section class="card card--front" aria-label="Business card, contact side">
    <div class="brand">
      <div class="lockup">
        <span class="lockup__mark" aria-hidden="true"></span>
        <span class="lockup__name">Marlow Behavioral Health</span>
      </div>
      <p class="tagline">Caring for mind, body and renewal</p>
    </div>
    <span class="divider" aria-hidden="true"></span>
    <div class="details">
      <h1 class="details__name">Daniel Reyes</h1>
      <p class="details__title">Founder &amp; CEO</p>
      <p class="details__address">2281 Orchard Lane Suite 140<br>Lakeview, TN 37010</p>
      <ul class="contact">
        <li>
          <svg viewBox="0 0 24 24" aria-hidden="true"><path d="M6.6 10.8a15.1 15.1 0 0 0 6.6 6.6l2.2-2.2a1 1 0 0 1 1-.25 11.4 11.4 0 0 0 3.6.57 1 1 0 0 1 1 1V20a1 1 0 0 1-1 1A17 17 0 0 1 3 4a1 1 0 0 1 1-1h3.5a1 1 0 0 1 1 1c0 1.250.2 2.460.57 3.58a1 1 0 0 1-.25 1z"/></svg>
          555-204-7781
        </li>
        <li>
          <svg viewBox="0 0 24 24" aria-hidden="true"><path d="M6 2h12v5H6zM3 8h18a1 1 0 0 1 1 1v8h-4v5H6v-5H2V9a1 1 0 0 1 1-1zm5 8v4h8v-4z"/></svg>
          555-204-7790
        </li>
        <li>
          <svg viewBox="0 0 24 24" aria-hidden="true"><path d="M2 5h20v14H2zm2 2v.4l8 5.1 8-5.1V7z"/></svg>
          hello@marlowbehavioral.com
        </li>
        <li>
          <svg viewBox="0 0 24 24" aria-hidden="true"><path d="M12 2a10 10 0 1 0 0 20 10 10 0 0 0 0-20zm0 2c.9 1.2 1.6 2.8 1.9 5h-3.8c.3-2.2 1-3.8 1.9-5zM4.3 13a8 8 0 0 1 0-2h3.8a17 17 0 0 0 0 2zm5.8 0a15 15 0 0 1 0-2h3.8a15 15 0 0 1 0 2zm5.8 0a17 17 0 0 0 0-2h3.8a8 8 0 0 1 0 2zM12 20c-.9-1.2-1.6-2.8-1.9-5h3.8c-.3 2.2-1 3.8-1.9 5z"/></svg>
          www.marlowbehavioral.com
        </li>
      </ul>
    </div>
  </section>

</body>
</html>
```